We need a full website with logo/graphics/woocommerce for hemp-based company

This site will be velmorix.com. It is a website featuring the fact we are the only manufacturer to produce CBDP and THCP. It should be great on mobile and desktop. We will pay for any extensions needed and while it should be a simple site:

About Us
About the Laboratory
About CBDP
About THCP
Shop
Contact Us

Only 4 products on the site.

It can be wordpress or joomla. Your choice. You must install the final website on our server. We agree to pay for monthly support that must be submitted in your quote.

He have a great graphics designer that will assist keeping colors and graphics clean according to your specifications.

Industry/Entity Type

Hemp CBD THC

Coding

Coded - Design and coding required

Number of Pages Required

5+ page

Requirements
Must have
• A simple clean layout

```html
<!DOCTYPE html>
<html lang="en">
<head>
<meta charset="utf-8">
<title>Contact Us – VELMORIX</title>
<link rel="stylesheet" href="https://fonts.googleapis.com/css2?family=Prata&family=Mulish:wght@400;600;700&display=swap">
<style>
:root{
  --green:#74bf1c;
  --green-dark:#5a9a12;
  --ink:#111111;
  --grey-panel:#ededed;
  --line:#dcdcdc;
  --white:#ffffff;
  --black:#000000;
  --footer-text:#e8e8e8;
}
*{box-sizing:border-box;margin:0;padding:0}
html,body{width:884px;height:1200px;overflow:hidden;background:var(--white)}
body{font-family:"Mulish",sans-serif;color:var(--ink);position:relative}
.abs{position:absolute}
.serif{font-family:"Prata",serif;font-weight:400}
svg{display:block}

.topbar{left:0;top:0;width:884px;height:22px;background:var(--green);color:var(--white);font-size:9px}
.topbar .item{position:absolute;top:5px;display:flex;align-items:center;gap:5px}
.topbar .right{font-weight:700}

.header{left:0;top:22px;width:884px;height:55px;background:var(--white)}
.brand{left:119px;top:14px;display:flex;align-items:center;gap:7px;font-family:"Prata",serif;font-size:20px;color:var(--green)}
.brand .dot{width:20px;height:20px;border-radius:50%;background:var(--green)}
.nav a{position:absolute;top:22px;font-size:9.3px;color:var(--ink);text-decoration:none;white-space:nowrap}
.nav a.active{color:var(--green);font-weight:700;border-bottom:1.5px solid var(--green);padding-bottom:3px}

.hero{left:0;top:77px;width:884px;height:194px;background:
  radial-gradient(ellipse at 55% 55%,#5f8a2c 0%,#3e6a1e 35%,transparent 70%),
  linear-gradient(90deg,#6f8a56 0%,#35581c 30%,#426e22 60%,#7d9470 100%)}

.crumbs{left:119px;top:290px;font-size:9.5px;display:flex;gap:12px}
.crumbs .current{color:var(--green);font-weight:700}

.page-title{left:0;top:348px;width:884px;text-align:center;font-size:27px}

.form-panel{left:119px;top:434px;width:338px;height:389px;background:var(--grey-panel)}
.form-panel h2{position:absolute;left:33px;top:30px;font-size:18px}
.form-panel p{position:absolute;left:33px;top:63px;font-size:8.3px}
.field{position:absolute;left:33px;width:271px;height:33px;background:var(--white);border:1px solid var(--line);font-size:8px;padding:11px 15px}
.field.message{height:55px}
.captcha{position:absolute;left:33px;top:288px;width:138px;height:33px;background:#f9f9f9;border:1px solid #d3d3d3;border-radius:2px;font-size:7px;display:flex;align-items:center;padding-left:6px;gap:6px}
.captcha .box{width:14px;height:14px;border:1.5px solid #c1c1c1;border-radius:2px;background:var(--white)}
.captcha .badge{position:absolute;right:8px;top:7px;width:16px;height:16px;border-radius:50%;background:#c9d6ea}
.submit{position:absolute;left:34px;top:332px;width:88px;height:29px;background:linear-gradient(180deg,#7fc61f,#6ab515);color:var(--white);font-weight:700;font-size:11px;display:flex;align-items:center;justify-content:center}

.info-panel{left:427px;top:403px;width:338px;height:387px;background:var(--green);color:var(--white)}
.info-panel .fold{position:absolute;left:0;top:0}
.info-panel h2{position:absolute;left:60px;font-size:19px}
.info-row{position:absolute;left:61px;display:flex;gap:14px;font-size:11px;line-height:16px}
.icon-disc{width:33px;height:33px;border-radius:50%;background:var(--white);display:flex;align-items:center;justify-content:center;flex:none}
.info-panel .rule{position:absolute;left:61px;top:253px;width:245px;height:1px;background:rgba(255,255,255,.35)}
.social{position:absolute;top:315px;width:26px;height:26px;border:1.5px solid var(--white);border-radius:50%}

.footer{left:0;top:879px;width:884px;height:321px;background:var(--black);color:var(--footer-text)}
.footer h3{position:absolute;top:52px;font-size:15px;color:var(--white)}
.links{position:absolute;left:120px;top:91px;list-style:none;font-size:9.3px}
.links li{height:20px;display:flex;gap:11px}
.links li::before{content:"›";font-size:10px}
.fcontact{position:absolute;left:267px;display:flex;gap:9px;font-size:9.3px;line-height:18px}
.fcontact .ico{width:14px;flex:none;display:flex;justify-content:center;padding-top:3px}
.fsocial{position:absolute;left:487px;display:flex;align-items:center;gap:9px;font-size:9.3px}
.fsocial .ring{width:26px;height:26px;border:1.5px solid var(--white);border-radius:50%}
.fbrand{left:646px;top:55px;width:118px;text-align:center;font-family:"Prata",serif;font-size:21px;color:var(--green)}
.fbrand .dot{width:44px;height:44px;border-radius:50%;background:var(--green);margin:0 auto 12px}
.footer .rule{position:absolute;left:119px;top:268px;width:647px;height:1px;background:#333}
.copyright{position:absolute;left:0;top:284px;width:884px;text-align:center;font-size:9px}
</style>
</head>
<body>

<div class="abs topbar">
  <div class="item" style="left:120px">
    <svg width="8" height="8" viewBox="0 0 24 24"><path fill="#fff" d="M6.6 10.8a15 15 0 0 0 6.6 6.6l2.2-2.2a1 1 0 0 1 1-.25 11.4 11.4 0 0 0 3.6.6 1 1 0 0 1 1 1V20a1 1 0 0 1-1 1A17 17 0 0 1 3 4a1 1 0 0 1 1-1h3.5a1 1 0 0 1 1 1c0 1.250.2 2.45.6 3.6a1 1 0 0 1-.25 1z"/></svg>
    +555 013 774
  </div>
  <div class="item" style="left:209px">
    <svg width="10" height="8" viewBox="0 0 24 18"><path fill="#fff" d="M0 0h24v2L12 10 0 2zM0 4.5l12 8 12-8V18H0z"/></svg>
    info@velmorix.com
  </div>
  <div class="item right" style="left:627px">
    <svg width="8" height="8" viewBox="0 0 24 24"><circle cx="12" cy="7" r="5" fill="#fff"/><path fill="#fff" d="M2 24c0-6 4-9 10-9s10 3 10 9z"/></svg>
    LOGIN &nbsp;|
  </div>
  <div class="item right" style="left:680px">
    <svg width="9" height="9" viewBox="0 0 24 24"><path fill="none" stroke="#fff" stroke-width="2.5" d="M4 2h11l5 5v15H4z"/></svg>
    REGISTER
  </div>
  <div class="item right" style="left:744px">
    <svg width="11" height="9" viewBox="0 0 24 20"><path fill="#fff" d="M0 7h24l-3 13H3zM7 7l5-7 5 7h-2l-3-4-3 4z"/></svg>
    0
  </div>
</div>

<header class="abs header">
  <div class="abs brand"><span class="dot"></span>VELMORIX</div>
  <nav class="nav">
    <a style="left:319px">Home</a>
    <a style="left:359px">About Us</a>
    <a style="left:414px">The Laboratory</a>
    <a style="left:498px">Sphaerophorol</a>
    <a style="left:577px">Rare Cannabinoids</a>
    <a style="left:675px">Shop</a>
    <a class="active" style="left:713px">Contact Us</a>
  </nav>
</header>

<div class="abs hero" role="img" aria-label="Close-up of green hemp plants growing in a greenhouse"></div>

<div class="abs crumbs"><span>Home</span><span>›</span><span class="current">Contact Us</span></div>

<h1 class="abs page-title serif">CONTACT US</h1>

<section class="abs form-panel">
  <h2 class="serif">GET IN TOUCH</h2>
  <p>Fill up the form and our team will get back to you within 24hours.</p>
  <div class="field" style="top:89px">Name*</div>
  <div class="field" style="top:133px">Phone*</div>
  <div class="field" style="top:177px">Email Address*</div>
  <div class="field message" style="top:221px">Message*</div>
  <div class="captcha"><span class="box"></span>I'm not a robot<span class="badge"></span></div>
  <div class="submit">Submit</div>
</section>

<section class="abs info-panel">
  <svg class="fold" width="31" height="31" viewBox="0 0 31 31"><path d="M0 0L31 31H0z" fill="var(--green-dark)"/></svg>
  <h2 class="serif" style="top:40px">CONTACT INFO</h2>

  <div class="info-row" style="top:83px">
    <div class="icon-disc"><svg width="12" height="15" viewBox="0 0 24 30"><path fill="var(--green)" d="M12 0a11 11 0 0 0-11 11c0 8 11 19 11 19s11-11 11-19A11 11 0 0 0 12 0zm0 15a4 4 0 1 1 0-8 4 4 0 0 1 0 8z"/></svg></div>
    <div>12 Lorem Ipsum, Street Name,<br>City Name, Country - 12345</div>
  </div>
  <div class="info-row" style="top:138px">
    <div class="icon-disc"><svg width="13" height="13" viewBox="0 0 24 24"><path fill="var(--green)" d="M6.6 10.8a15 15 0 0 0 6.6 6.6l2.2-2.2a1 1 0 0 1 1-.25 11.4 11.4 0 0 0 3.6.6 1 1 0 0 1 1 1V20a1 1 0 0 1-1 1A17 17 0 0 1 3 4a1 1 0 0 1 1-1h3.5a1 1 0 0 1 1 1c0 1.25.2 2.45.6 3.6a1 1 0 0 1-.25 1z"/></svg></div>
    <div>PHONE<br>(555) 014-2290</div>
  </div>
  <div class="info-row" style="top:194px">
    <div class="icon-disc"><svg width="14" height="11" viewBox="0 0 24 18"><path fill="var(--green)" d="M0 0h24v2L12 10 0 2zM0 4.5l12 8 12-8V18H0z"/></svg></div>
    <div>EMAIL<br>info@velmorix.com</div>
  </div>

  <div class="rule"></div>
  <h2 class="serif" style="top:276px">FOLLOW US</h2>
  <span class="social" style="left:60px"></span>
  <span class="social" style="left:93px"></span>
  <span class="social" style="left:126px"></span>
</section>

<footer class="abs footer">
  <h3 class="serif" style="left:120px">QUICK LINKS</h3>
  <ul class="links">
    <li>Home</li><li>About Us</li><li>The Laboratory</li><li>Sphaerophorol</li><li>Rare Cannabinoids</li><li>Shop</li><li>Contact Us</li>
  </ul>

  <h3 class="serif" style="left:266px">CONTACT DETAILS</h3>
  <div class="fcontact" style="top:89px">
    <span class="ico"><svg width="10" height="14" viewBox="0 0 24 30"><path fill="#fff" d="M12 0a11 11 0 0 0-11 11c0 8 11 19 11 19s11-11 11-19A11 11 0 0 0 12 0zm0 15a4 4 0 1 1 0-8 4 4 0 0 1 0 8z"/></svg></span>
    <div>12 Lorem Ipsum, Street Name,<br>City Name, Country - 12345</div>
  </div>
  <div class="fcontact" style="top:138px">
    <span class="ico"><svg width="11" height="11" viewBox="0 0 24 24"><path fill="#fff" d="M6.6 10.8a15 15 0 0 0 6.6 6.6l2.2-2.2a1 1 0 0 1 1-.25 11.4 11.4 0 0 0 3.6.6 1 1 0 0 1 1 1V20a1 1 0 0 1-1 1A17 17 0 0 1 3 4a1 1 0 0 1 1-1h3.5a1 1 0 0 1 1 1c0 1.25.2 2.45.6 3.6a1 1 0 0 1-.25 1z"/></svg></span>
    <div>PHONE<br>(555) 014-2290</div>
  </div>
  <div class="fcontact" style="top:184px">
    <span class="ico"><svg width="13" height="10" viewBox="0 0 24 18"><path fill="#fff" d="M0 0h24v2L12 10 0 2zM0 4.5l12 8 12-8V18H0z"/></svg></span>
    <div>EMAIL<br>info@velmorix.com</div>
  </div>

  <h3 class="serif" style="left:485px">FOLLOW US ON</h3>
  <div class="fsocial" style="top:88px"><span class="ring"></span>Friendora</div>
  <div class="fsocial" style="top:131px"><span class="ring"></span>Chirplet</div>
  <div class="fsocial" style="top:174px"><span class="ring"></span>Snapvista</div>

  <div class="abs fbrand"><div class="dot"></div>VELMORIX</div>

  <div class="rule"></div>
  <p class="copyright">© 2021 VELMORIX. All Rights Reserved.</p>
</footer>

</body>
</html>
```